The Pebble Finch Leaflet. A5 2-sided Flyer for a UK Lawn Treatment Company

I need an A5 two-side leaflet / flyer designed for my Lawn Treatment company. The leaflet will be for door-drops so quick impact needed. Full colour, both sides. I provide lawn treatments to customers in the Exeter area of Devon. I would like to design to be clear, fresh and reflect the joy a good lawn and garden can bring.

Target Market(s)

Home Owners. 30-80 Years. Familys

Font styles to use
Sans Serif

Colors
9bcb3c
f78f20
ec1f27
33a6d7

Requirements
Must have
• Good front page picture
• Logo
• Contact details on front.
• Call to Action
• More details in Text file included in design.
Nice to have
• Clipart of a family / lady enjoying a lawn.

```html
<!DOCTYPE html>
<html lang="en">
<head>
<meta charset="utf-8">
<title>The Pebble Finch – Lawn Treatment Leaflet</title>
<link href="https://fonts.googleapis.com/css2?family=Roboto:wght@400;500;700&family=Open+Sans:wght@400;600;700&display=swap" rel="stylesheet">
<style>
  :root{
    --bg:#e9e9e9;
    --white:#ffffff;
    --green:#3aa746;
    --green-deep:#16783a;
    --green-dark:#146b34;
    --green-pale:#b8dca3;
    --leaf:#9bcb3c;
    --orange:#f7a21b;
    --gold:#f5b21a;
    --gold-dark:#c98a12;
    --brown:#6b2a16;
    --ink-green:#1e6b34;
    --text:#ffffff;
    --head:"Roboto",Arial,sans-serif;
    --body:"Open Sans",Arial,sans-serif;
  }
  *{box-sizing:border-box;margin:0;padding:0}
  html,body{width:1200px;height:825px;overflow:hidden;background:var(--bg)}
  body{position:relative;font-family:var(--body)}
  .page{position:absolute;top:92px;width:468px;height:638px;overflow:hidden;box-shadow:0 2px 6px rgba(0,0,0,.25)}
  .front{left:100px;background:var(--white)}
  .back{left:634px;background:var(--green-deep)}

  /* FRONT */
  .hero-photo{position:absolute;left:0;top:0;width:468px;height:335px}
  .header-curve{position:absolute;left:0;top:0;width:468px;height:110px}
  .brand{position:absolute;left:22px;top:28px;display:flex;align-items:center;gap:8px}
  .brand-dot{width:26px;height:26px;border-radius:50%;background:var(--leaf)}
  .brand-name{font-family:var(--head);font-weight:500;font-size:19px;color:var(--ink-green)}
  .badge{position:absolute;right:16px;top:6px;width:96px;height:96px}
  .green-body{position:absolute;left:0;top:330px;width:468px;height:262px;background:var(--green)}
  .headline-box{position:absolute;left:20px;top:333px;width:430px;height:70px;background:var(--white);border-radius:0 0 12px 12px;text-align:center;box-shadow:0 2px 3px rgba(0,0,0,.2)}
  .headline-main{font-family:var(--head);font-weight:500;font-size:29px;color:var(--ink-green);line-height:32px;margin-top:5px;letter-spacing:.5px}
  .headline-sub{font-family:var(--head);font-size:22px;color:var(--ink-green);line-height:26px}
  .new-area{position:absolute;left:20px;top:420px;font-family:var(--head);font-size:19px;line-height:20px;color:var(--white)}
  .experience{position:absolute;left:193px;top:416px;width:290px;height:46px;border:2px dashed var(--green-dark);border-radius:6px;padding:4px 0 0 18px;font-family:var(--head);font-size:14.5px;line-height:18px;color:var(--white)}
  .lawn-thumb{position:absolute;top:473px;width:126px;height:72px;border:3px solid var(--white);border-radius:6px}
  .thumb-1{left:22px;background:linear-gradient(180deg,#6f8a5a 0%,#5fa63a 35%,#7cc24a 100%)}
  .thumb-2{left:171px;background:linear-gradient(180deg,#3f6e2f 0%,#6ea548 45%,#8cc158 100%)}
  .thumb-3{left:320px;background:linear-gradient(180deg,#b8c9d8 0%,#3f6e2f 30%,#73ad45 100%)}
  .call-line{position:absolute;left:34px;top:556px;font-family:var(--head);font-size:12.5px;color:var(--white);letter-spacing:.4px;white-space:nowrap}
  .call-line strong{font-weight:400;font-size:17px;color:var(--brown)}
  .foot-band{position:absolute;left:0;top:590px;width:468px;height:48px;background:var(--green-dark)}
  .foot-label{position:absolute;left:32px;top:604px;font-family:var(--head);font-size:13px;color:var(--white)}
  .foot-tab{position:absolute;left:214px;top:597px;width:254px;height:41px;background:var(--white);border-radius:14px 0 0 0;text-align:center;font-family:var(--head);font-size:19px;line-height:40px;color:var(--ink-green)}

  /* BACK */
  .back-content{position:absolute;left:15px;top:10px;width:440px;color:var(--text)}
  .back-title{font-family:var(--head);font-weight:400;font-size:22px;line-height:26px;color:var(--orange)}
  .back-text{font-size:11.6px;line-height:13.4px;text-align:justify;margin-bottom:4px}
  .back-text .phone{font-size:14px}
  .treatments{position:absolute;left:20px;top:318px;list-style:none;font-family:var(--head);font-size:15px;line-height:17.6px;color:var(--white)}
  .treatments li::before{content:"";display:inline-block;width:7px;height:7px;border-radius:50%;background:var(--gold);margin-right:7px;vertical-align:2px}
  .cta-swoosh{position:absolute;left:0;top:460px;width:468px;height:178px}
  .cta-box{position:absolute;left:24px;top:491px;width:246px;height:67px;background:var(--brown);border-radius:14px 0 0 0;padding:6px 0 0 22px;font-family:var(--body);font-weight:700;font-size:17px;line-height:18px;color:var(--white)}
  .cta-call{position:absolute;left:68px;top:570px;font-weight:700;font-size:12px;color:#1a1a1a;white-space:nowrap}
  .cta-call strong{font-family:var(--head);font-weight:500;font-size:16px;color:var(--brown)}
  .back-url{position:absolute;left:66px;top:606px;font-family:var(--head);font-size:19px;color:var(--gold)}
  .testimonials{position:absolute;left:268px;top:318px;width:200px;height:320px;background:var(--gold);border-radius:14px 0 0 0;padding:10px 10px 0 10px;color:#3a2410;text-align:justify}
  .testimonials h2{font-family:var(--head);font-weight:400;font-size:18px;text-align:center;color:var(--brown);margin-bottom:8px}
  .quote{font-size:10px;line-height:13.5px;margin-bottom:8px}
  .quote b{font-weight:700;font-size:11.5px;color:var(--brown)}
</style>
</head>
<body>

<section class="page front" aria-label="Leaflet front">
  <div class="hero-photo" role="img" aria-label="Photo of a family playing football together on a sunny green lawn" style="background:linear-gradient(180deg,#8fb7d9 0%,#b9a48a 30%,#7a5a45 55%,#5b8a3a 75%,#6fae3c 100%)"></div>
  <svg class="header-curve" viewBox="0 0 468 110" aria-hidden="true">
    <path d="M0 0 H468 V8 C380 30 300 80 180 95 C110 102 50 98 0 92 Z" fill="var(--white)"/>
    <path d="M0 92 C50 98 110 102 180 95 C300 80 380 30 468 8 V16 C380 40 300 90 180 103 C110 110 50 104 0 98 Z" fill="var(--green)"/>
  </svg>
  <div class="brand">
    <span class="brand-dot"></span>
    <span class="brand-name">The Pebble Finch</span>
  </div>
  <svg class="badge" viewBox="0 0 96 96" aria-hidden="true">
    <circle cx="48" cy="48" r="44" fill="var(--gold-dark)"/>
    <circle cx="48" cy="48" r="36" fill="var(--gold)"/>
    <rect x="0" y="38" width="96" height="22" rx="3" fill="var(--brown)" transform="rotate(-14 48 48)"/>
  </svg>

  <div class="green-body"></div>
  <div class="headline-box">
    <p class="headline-main">TREATMENTS AND ADVICE</p>
    <p class="headline-sub">to keep your lawn looking nice.</p>
  </div>
  <p class="new-area">BRAND NEW<br>TO THE AREA!</p>
  <p class="experience">8 Years experience maintaining<br>the finest lawns of Exeter</p>
  <div class="lawn-thumb thumb-1" role="img" aria-label="Striped mown lawn in a formal garden"></div>
  <div class="lawn-thumb thumb-2" role="img" aria-label="Lawn with a gravel path and summer house"></div>
  <div class="lawn-thumb thumb-3" role="img" aria-label="Lawn bordered by tall clipped hedges"></div>
  <p class="call-line">CALL TODAY ON <strong>01632 960418</strong> OR TEXT <strong>07700 900312</strong></p>
  <div class="foot-band"></div>
  <p class="foot-label">book your lawn survey</p>
  <p class="foot-tab">thepebblefinch.co.uk</p>
</section>

<section class="page back" aria-label="Leaflet back">
  <div class="back-content">
    <h2 class="back-title">For a beautiful weed-free lawn</h2>
    <p class="back-text">Call The Pebble Finch today and start your journey to a wonderful, lush, green lawn you and your family can enjoy.</p>
    <p class="back-text">Arrange a no-obligation lawn survey and quotation at a time to suit you. Call <span class="phone">01632 960418</span> now.</p>
    <h2 class="back-title">I will understand your lawn</h2>
    <p class="back-text">Every lawn is unique. I take time to gain a comprehensive understanding of your lawn and its situation. I will also listen to you and understand your problems and your aspirations for your grass.</p>
    <h2 class="back-title">Your lawn treatments</h2>
    <p class="back-text">I will creat a custom treatment programme tailored to your lawn. I may also recommend some remedial treatments to correct any existing problems. There is no contract to sign. I guarantee all treatments.</p>
    <h2 class="back-title">Industry-leading lawn care</h2>
    <p class="back-text">I have 8 years of experience in the leading edge of domestic lawn care. I have a comprehensive range of treatments including:</p>
  </div>
  <ul class="treatments">
    <li>Scarification</li>
    <li>Aeration</li>
    <li>Moss Control</li>
    <li>Overseeding</li>
    <li>Top Dressing</li>
    <li>Lawn Repairs</li>
    <li>Fertilisation &amp; Weed Control</li>
    <li>Pest and Disease Management</li>
    <li>Special Event Preparation</li>
  </ul>

  <svg class="cta-swoosh" viewBox="0 0 468 178" aria-hidden="true">
    <path d="M0 178 C15 105 110 88 268 76 V90 C120 96 30 110 8 178 Z" fill="var(--gold)"/>
    <path d="M10 178 C30 110 120 96 268 90 V134 C120 134 50 140 30 178 Z" fill="var(--green-pale)"/>
  </svg>
  <p class="cta-box">Save time and money<br>and leave your lawn to<br>an expert.</p>
  <p class="cta-call">Call <strong>01632 960418</strong> Today.</p>
  <p class="back-url">thepebblefinch.co.uk</p>

  <aside class="testimonials">
    <h2>TESTIMONIALS:</h2>
    <p class="quote">Thank you for keeping our lawn in great shape for so long, I've been really pleased with how it has looked since you took care of it. <b>Owen</b></p>
    <p class="quote">My lawn has never looked better since the day that you started to look after it for me. <b>Mrs. Vale</b></p>
    <p class="quote">We are so grateful for your skill over the years. We've seen our lawn thrive and you changed a neglected difficult garden to one that everyone comments on. <b>Morwen</b></p>
    <p class="quote">We have very much appreciated your service over the last four years, and especially value your reliability and perennial cheerfulness! <b>Bramwell</b></p>
  </aside>
</section>

</body>
</html>
```